Business card design can get creative with spot gloss, foil, metallic details, colored edge details, different shapes, imprint, etc. Open to creativity. Needs to look professional, elegant, sophisticated, and current.
Also, needs to be easy to read for a 40+ clientele. No strange or hard to read fonts.
If we get exceptional designs for the individual items we have asked for from different designers, we will choose more than one winner.
We realize now, it may not be possible to get all of the individual items we asked for from the same designer and that is ok.
Thanks everyone, we are overwhelmed by great designs.
What we like is a horizontal layout, not vertical, clean lines or minimal wave design. We like the web site address in white print on black, so it stands out and does not get lost with all the other information.
We also like a straight edge over a rounded corner. Can be glossy- if so- we may list services not next appointment on the back. It's too difficult & not practical for the appointment to be on glossy paper- hard to write on. We may opt to then have a separate appointment card- matte finish.
We are leaning towards only listing our local phone number the 555-019-2846, it's getting too cluttered with both local and toll free number.
Keep in mind the basic design of the card has to look good and balanced to print the card with and without the managers name. So that way we have the basic design for the boutique card and can change the employee information/name as appropriate.
The small addition of a touch of purple we like, as in #164.
We just need it to have a professional look not a casual feel to it.
I want to show that we are cutting edge, hip and up on the latest technology to stay connected to our clients and make it easy for them to reach us.

```html
<!DOCTYPE html>
<html lang="en">
<head>
<meta charset="utf-8">
<title>The Willow Nest – Stationery Concept</title>
<link href="https://fonts.googleapis.com/css2?family=Questrial&display=swap" rel="stylesheet">
<style>
  :root {
    --lime: #9bcb1c;
    --lime-soft: #eef6dc;
    --charcoal: #2f2b2c;
    --paper: #ffffff;
    --ink: #555555;
    --board: #7b7b7b;
    --board-light: #b9b9b9;
    --label: #e8e8e8;
  }
  * { box-sizing: border-box; margin: 0; padding: 0; }
  html, body { width: 1200px; height: 386px; overflow: hidden; }
  body {
    font-family: "Questrial", Arial, sans-serif;
    background: radial-gradient(ellipse at 50% 40%, var(--board-light), var(--board));
    position: relative;
  }
  .item { position: absolute; box-shadow: 0 2px 6px rgba(0,0,0,.35); }
  .label { position: absolute; font-size: 6px; color: var(--label); }

  .brand { color: var(--lime); line-height: .95; display: flex; align-items: center; gap: 4px; }
  .brand .dot { width: 10px; height: 10px; border-radius: 50%; background: var(--lime); flex: none; }

  /* business cards */
  .card { width: 170px; height: 92px; padding: 9px 10px; font-size: 6px; }
  .card--dark { background: var(--charcoal); color: #fff; }
  .card--framed { background: var(--paper); color: var(--ink); border: 4px solid var(--lime); }
  .card--front { background: var(--paper); color: var(--ink); overflow: hidden; }
  .card h4 { color: var(--lime); font-size: 7px; font-weight: 400; margin: 2px 0; }
  .card .list { display: flex; gap: 10px; margin-bottom: 5px; }
  .card .line { border-bottom: 1px solid currentColor; opacity: .6; width: 60px; display: inline-block; margin-left: 3px; }
  .card--front .brand { font-size: 13px; }
  .card--front .strip { position: absolute; right: 0; top: 0; width: 34px; height: 100%; background: var(--lime); }
  .card--front .info { position: absolute; left: 10px; bottom: 8px; }
  .web { background: var(--charcoal); color: #fff; padding: 1px 4px; display: inline-block; margin-top: 2px; }

  .concept { position: absolute; left: 195px; top: 80px; }
  .concept .brand { font-size: 20px; }
  .concept p { color: #fff; font-size: 13px; margin-top: 10px; }

  /* letterheads */
  .letter { width: 180px; height: 352px; background: var(--paper); top: 12px; }
  .letter .brand { position: absolute; left: 14px; top: 14px; font-size: 15px; }
  .letter .contact { position: absolute; left: 90px; top: 16px; font-size: 5px; color: var(--ink); line-height: 1.5; }
  .letter .side { position: absolute; right: 0; top: 0; width: 14px; height: 96px; background: var(--lime); }
  .letter .foot { position: absolute; left: 0; bottom: 0; width: 100%; height: 6px; background: var(--lime); }
  .letter .mark { position: absolute; left: 40px; top: 125px; width: 100px; height: 100px; border-radius: 50%; background: var(--lime-soft); }

  /* envelopes */
  .envelope { background: var(--paper); overflow: hidden; }
  .envelope svg { position: absolute; left: 0; top: 0; }
  .envelope .brand { position: absolute; font-size: 9px; }
</style>
</head>
<body>

  <!-- business cards -->
  <div class="item card card--dark" style="left:12px;top:62px">
    <h4>Services</h4>
    <div class="list"><span>Maternity Wear</span><span>Nursing Bras</span></div>
    <div class="list"><span>Baby Gifts</span><span>Belly Casts</span></div>
    <h4>Next Appointment</h4>
    <div>Date<span class="line"></span></div>
    <div style="margin-top:4px">Time<span class="line"></span></div>
  </div>
  <span class="label" style="left:12px;top:157px">Business Card Back</span>

  <div class="concept">
    <div class="brand"><span class="dot"></span><span>the<br>willow<br>nest</span></div>
    <p>Stationery Concept</p>
  </div>

  <div class="item card card--framed" style="left:12px;top:170px">
    <h4>Services</h4>
    <div class="list"><span>Maternity Wear</span><span>Nursing Bras</span></div>
    <div class="list"><span>Baby Gifts</span><span>Belly Casts</span></div>
    <h4>Next Appointment</h4>
    <div>Date<span class="line"></span></div>
    <div style="margin-top:4px">Time<span class="line"></span></div>
  </div>
  <span class="label" style="left:12px;top:265px">Business Card Back</span>

  <div class="item card card--front" style="left:192px;top:170px">
    <div class="brand"><span class="dot"></span><span>the<br>willow nest</span></div>
    <div class="info">Store Manager<br>555-019-2846<br><span class="web">willownest.com</span></div>
    <div class="strip"></div>
  </div>
  <span class="label" style="left:192px;top:265px">Business Card Front</span>

  <div class="item card card--front" style="left:12px;top:278px">
    <h4>Your Next Appointment</h4>
    <div style="margin-top:10px">Date<span class="line"></span></div>
    <div style="margin-top:8px">Time<span class="line"></span></div>
    <div class="strip" style="width:14px"></div>
  </div>
  <span class="label" style="left:12px;top:373px">Appointment Card Back</span>

  <div class="item card card--front" style="left:192px;top:278px">
    <div class="brand"><span class="dot"></span><span>the<br>willow nest</span></div>
    <div class="info">555-019-2846<br><span class="web">willownest.com</span></div>
    <div class="strip"></div>
  </div>
  <span class="label" style="left:192px;top:373px">Appointment Card Front</span>

  <!-- letterheads -->
  <div class="item letter" style="left:370px">
    <div class="brand"><span class="dot"></span><span>the<br>willow<br>nest</span></div>
    <div class="contact">12 Orchard Lane<br>555-019-2846<br>hello@willownest.com</div>
    <div class="side"></div>
    <div class="mark" role="img" aria-label="Faint brand emblem watermark"></div>
    <div class="foot"></div>
  </div>
  <span class="label" style="left:370px;top:368px">Letterhead Page One</span>

  <div class="item letter" style="left:565px">
    <div class="brand"><span class="dot"></span><span>the<br>willow<br>nest</span></div>
    <div class="contact">Springfield<br>555-019-2846<br>hello@willownest.com</div>
    <div class="side"></div>
    <div class="mark" role="img" aria-label="Faint brand emblem watermark"></div>
    <div class="foot"></div>
  </div>
  <span class="label" style="left:565px;top:368px">Letterhead Page Two</span>

  <!-- envelopes -->
  <div class="item envelope" style="left:770px;top:150px;width:230px;height:110px">
    <svg width="230" height="110"><polyline points="0,0 115,60 230,0" fill="none" stroke="#ddd"/></svg>
    <div class="brand" style="left:12px;top:78px"><span class="dot"></span><span>the willow nest</span></div>
  </div>

  <div class="item envelope" style="left:960px;top:135px;width:225px;height:105px">
    <svg width="225" height="105"><polygon points="0,0 225,0 112,55" fill="#2f2b2c"/></svg>
    <div class="brand" style="left:100px;top:8px"><span class="dot"></span></div>
  </div>

  <div class="item envelope" style="left:960px;top:248px;width:225px;height:70px">
    <svg width="225" height="70"><polygon points="0,0 225,0 112,32" fill="#f2f2f2" stroke="#ddd"/></svg>
    <div class="brand" style="left:12px;top:50px"><span class="dot"></span><span>the willow nest</span></div>
  </div>

  <div class="item envelope" style="left:770px;top:295px;width:200px;height:62px">
    <svg width="200" height="62"><polygon points="0,0 200,0 100,28" fill="#9bcb1c"/></svg>
    <div class="brand" style="left:10px;top:44px"><span class="dot"></span><span>the willow nest</span></div>
  </div>
  <span class="label" style="left:770px;top:362px">Envelope Set</span>

</body>
</html>
```